New doctor needs elegant, whimsical Business Card Design

CHALLENGE: how to highlight gynaecological service (use of abstract cervix in logo?) in NON-VULGAR way + project an elegant, professional tone?

We need a business card design (incl logo) for a gynaecologist who is starting his private practice. The main area of service will be colposcopy - a diagnostic procedure using a microscope to look at the tissues of the cervix for any potentially cancerous cells.

STYLE: Classic, elegant, timeless look. Fairly simple, not too cluttered. Logo NOT to overpower name. Want to project a professional but approachable image - "gentleman". Not too "corporate" - whimsical, without becoming feminine.

COLOUR: soft colours - no clashing primary colours, nothing too "brash" or commercial.
White background/black lettering + 1 colour accent, pattern repeated throughout card, in both logo & text (refer to "mock-up example" image file)
The colour accent should be BLUE: a serene/calm but confident shade: eg. strong pastel blue, dark baby blue (NOT royal blue, navy, turquoise, aquamarine, etc)

TEXT: have a calligraphy feel (but not too fancy as to be difficult to read at a glance) or more italics/rounded edges kind of font (refer to refer to "mock-up example" image file)
- Contrast between NAME in more italic font Vs. rest of text in "straight" print (or vice versa)

LOGO:
1) something very similar to "The Wren Trust" logo (ref image attached) - an abstract, black line drawing of a woman's figure, with a single, coloured symbol. No detail in line drawing - NO head or arms - don't want it to be obviously women's figure - want it very stylised, abstract, fluid lines.

* The Wren Trust used a heart but we would like to use an another symbol in BLUE - maybe an abstract of a cervix? eg. the "triangle" shape symbol (see the image file of the Silver Thread Wellness Initiative - the symbol in the middle of the flower) OR the "donut" representation of the cervix (see notes below)

BUT - don't want the symbol exactly over the groin area, otherwise looks vulgar. Don't want it to look like bikini or genitals! Symbol should be incorporated into line drawing but NOT drawing direct attention to the groin. Maybe displaced to one side? Or further up the body? Open to your ideas

2) We are also open to any other ideas you may have, of stylistic/abstract designs based on:
- the image of a cervix (looks very similar to a pink donut - usually shown in medical shorthand as a tiny circle in the middle of a bigger circle.)
- the cervix with some cells within ? Some stylised version of cancer cells?
(please see attached selection of images for reference/inspiration)

2 main audiences: women (18 - 70) concerned about abnormal PAP smear, other gynae-issues, 2) GP's referring their patients to a gynae-specialist

Medical

• ONE side only - Reverse of business card must be kept blank for "Appointments" notes.

• NO "retro" American feel - nor anything 60's or 70's kind of feel. Don't want fonts that look too commercial or industrial/harsh.

Logo: NO obvious silhouettes/profiles of women (abstract is OK but not detail), NO female reproductive system (2 ovaries & uterus), no female symbol - as these are the usual cliches for gynaecologists.

DON'T want the symbol exactly over the groin area, otherwise looks vulgar. Don't want it to look like bikini or genitals! Symbol should be incorporated into line drawing but NOT drawing direct attention to the groin. Maybe displaced to one side? Or further up the body? Open to your ideas

```html
<!DOCTYPE html>
<html lang="en">
<head>
<meta charset="utf-8">
<title>Dr Adrian Hale – Business Card</title>
<link rel="stylesheet" href="https://fonts.googleapis.com/css2?family=Kalam:wght@300&family=Encode+Sans+Condensed:wght@300&family=Open+Sans:wght@400;700&display=swap">
<style>
  :root {
    --backdrop: #777777;
    --card: #ffffff;
    --blue: #4a8db5;
    --grey-text: #6b6b6b;
    --figure-tone: #f1f1f1;
    --symbol-pink: #f3d2e0;
    --rule: #4a86b0;
  }
  * { margin: 0; padding: 0; box-sizing: border-box; }
  html, body {
    width: 1200px; height: 1000px; overflow: hidden;
    background: var(--backdrop);
  }
  .card {
    position: absolute;
    width: 673px; height: 384px;
    background: var(--card);
    overflow: hidden;
  }
  .card--front { left: 98px; top: 95px; }
  .card--back { left: 457px; top: 559px; }

  /* Placeholder for the logo figure and its symbol */
  .figure-art {
    position: absolute; left: 0; top: 0;
    width: 150px; height: 100%;
    background:
      radial-gradient(ellipse 70px 50px at 12px 265px, var(--symbol-pink) 55%, rgba(243,210,224,0) 100%),
      linear-gradient(90deg, var(--figure-tone) 75%, rgba(241,241,241,0));
  }

  .name {
    position: absolute; right: 16px; top: 42px;
    font-family: "Kalam", cursive; font-weight: 300;
    font-size: 52px; color: var(--blue);
    letter-spacing: 3px; line-height: 1.1;
    white-space: nowrap;
  }
  .specialty {
    position: absolute; right: 18px; top: 106px;
    font-family: "Open Sans", sans-serif;
    font-size: 18px; letter-spacing: 2px;
    color: var(--grey-text);
  }
  .credentials {
    position: absolute; right: 16px; top: 132px;
    font-family: "Encode Sans Condensed", sans-serif; font-weight: 300;
    font-size: 18.5px; color: var(--blue);
    white-space: nowrap;
  }
  .contact, .address {
    position: absolute; left: 0; width: 673px;
    text-align: center;
    font-family: "Encode Sans Condensed", sans-serif; font-weight: 300;
    font-size: 19px; white-space: nowrap;
  }
  .contact { top: 312px; color: var(--blue); padding-left: 2px; }
  .address { top: 345px; color: var(--grey-text); }

  .appointments-title {
    position: absolute; top: 14px; left: 0; width: 673px;
    text-align: center;
    font-family: "Open Sans", sans-serif; font-weight: 700;
    font-size: 18px; letter-spacing: 1.8px; color: var(--grey-text);
  }
  .column-head {
    position: absolute; top: 56px;
    font-family: "Open Sans", sans-serif;
    font-size: 19px; letter-spacing: 1px; color: var(--blue);
  }
  .column-head--date { left: 138px; }
  .column-head--time { left: 481px; }
  .entry-rules { position: absolute; left: 0; top: 0; }
  .website {
    position: absolute; top: 353px; left: 0; width: 673px;
    text-align: center;
    font-family: "Open Sans", sans-serif;
    font-size: 18px; letter-spacing: 0.6px; color: var(--blue);
  }
</style>
</head>
<body>
  <section class="card card--front">
    <div class="figure-art" role="img" aria-label="Practice emblem: faint abstract figure outline with a soft pink symbol"></div>
    <h1 class="name">Dr Adrian Hale</h1>
    <p class="specialty">GYNAECOLOGIST</p>
    <p class="credentials">MB BCh - MA(Oxon) - Dip Obs -FRANZCOG - MD</p>
    <p class="contact">T +61 8 61002481 | F +61 8 61002487 | admin@halegynae.com.au</p>
    <p class="address">Suite 12 | Lindenwood Medical Centre | 40 Carrow Ave | Ashgrove, WA 6011</p>
  </section>

  <section class="card card--back">
    <div class="figure-art" role="img" aria-label="Practice emblem: faint abstract figure outline with a soft pink symbol"></div>
    <h2 class="appointments-title">APPOINTMENTS</h2>
    <span class="column-head column-head--date">DATE</span>
    <span class="column-head column-head--time">TIME</span>
    <svg class="entry-rules" width="673" height="384" aria-hidden="true">
      <g stroke="var(--rule)" stroke-width="1.5">
        <line x1="0" y1="91" x2="673" y2="91"/>
        <line x1="0" y1="127" x2="673" y2="127"/>
        <line x1="0" y1="165" x2="673" y2="165"/>
        <line x1="0" y1="203" x2="673" y2="203"/>
        <line x1="0" y1="240" x2="673" y2="240"/>
        <line x1="0" y1="277" x2="673" y2="277"/>
      </g>
    </svg>
    <p class="website">Halegynae.com.au</p>
  </section>
</body>
</html>
```